Glazmor signs for fridge and desk

I require 3 a4 designs very basic designs with single colour and easy to print. I have atached a style guide to see the fonts I used in my last three design. Please remember I'm printing in only one colour
PLease see the following link, of what I sell on zorblu. I will be selling this allong side these products.
https://www.zorblu.com/gp/item/K52QX8RMVA
Please see my competitors
https://www.zorblu.com/Memo-Sticky-Schedule-Cooler-Holder/it/K9TRW4HQDP/ref=sr_1_8?keywords=clear%2Bmemo%2Bpanel%2Bcooler%2Bwipe%2Bclean%2Bpanel%2Bsticky%2Bsee&qid=1600112233&sr=8-8&th=1
and
https://www.zorblu.com/Sticky-Clear-Schedule-Cooler-Chiller/it/K7MPQ2XTRD/ref=sr_1_4_sp?keywords=clear+memo+panel+cooler+wipe+clean+panel+sticky+see&qid=1600114455&sr=8-4-promo&psc=1&spLa=QmxhaGJsYWhibGFoYmxhaGJsYWhibGFoYmxhaGJsYWhibGFoYmxhaGJsYWhibGFoYmxhaGJsYWhibGFoYmxhaGJsYWhibGFoYmxhaGJsYWhibGFoYmxhaGJsYWhibGFoYmxhaGJsYWhibGFoYmxhaGJsYWhibGFoYmxhaGJsYWhibGFoYmxhaGJsYWhibGFoYmxhaGJsYWhibGFoYmxhaGJsYWg=
I'd like something more fun and different. But that can still be printed on Glazmor with one colour and be functional. A shopping list, a weekly planner(both that stick to a fridge) and a to do list that will sit on a desk or kitchen counter top.
PLease design
1st a4
Break into seven parts, with seven headings..... Monday to Sunday.... here customers will be able to write menus and upcoming events. I want this landcape
2nd a4
'Shopping List' is to be the heading
I want this landcape
3rd a4
'To Do List' is the only text I would like
I would like this portrat and lines marked and a check box on the left hand side
Remember I can only print on the acrylic with one colour. I want to be different from my competitors but I do want to be functional.
just a reminder. I can only print with one colour

```html
<!DOCTYPE html>
<html lang="en">
<head>
<meta charset="UTF-8">
<title>To Do List</title>
<link rel="stylesheet" href="https://fonts.googleapis.com/css2?family=Roboto+Condensed:wght@900&display=swap">
<style>
  :root {
    --ink: #000000;
    --paper: #ffffff;
  }
  html, body {
    margin: 0;
    padding: 0;
    width: 849px;
    height: 1200px;
    overflow: hidden;
    background: var(--paper);
  }
  .todo-sheet {
    position: relative;
    width: 849px;
    height: 1200px;
    background: var(--paper);
  }
  .sheet-art {
    position: absolute;
    inset: 0;
    width: 849px;
    height: 1200px;
  }
  .sheet-title {
    position: absolute;
    left: 292px;
    top: 48px;
    width: 250px;
    margin: 0;
    text-align: center;
    font-family: "Roboto Condensed", "Arial Narrow", sans-serif;
    font-weight: 900;
    font-size: 62px;
    line-height: 62px;
    letter-spacing: -1px;
    color: var(--ink);
  }
  .sheet-title span { display: block; }
</style>
</head>
<body>
  <main class="todo-sheet">
    <svg class="sheet-art" viewBox="0 0 849 1200" xmlns="http://www.w3.org/2000/svg" aria-hidden="true">
      <g fill="none" stroke="var(--ink)">
        <rect class="frame" x="26.2" y="26.2" width="798" height="1150" rx="41" stroke-width="3.2"/>
        <rect class="header-box" x="102.5" y="86.5" width="54.5" height="54.5" rx="14" stroke-width="2.2"/>
      </g>
      <path class="header-tick" fill="var(--ink)"
            d="M97 111.5 C108 111.5 117 116 122 124 C135 97 160 80 197 79.5 C165 84 139 101 123 134 L121 128 C118 118 110 112 97 111.5 Z"/>

      <g class="rows" fill="none" stroke="var(--ink)" stroke-width="2">
        <g class="row">
          <rect x="50.8" y="191.8" width="749.3" height="180.7" rx="21"/>
          <line x1="202.3" y1="191.8" x2="202.3" y2="372.5"/>
          <rect class="checkbox" x="102.7" y="259" width="49.8" height="50" rx="15"/>
        </g>
        <g class="row">
          <rect x="50.8" y="387.8" width="749.3" height="180" rx="21"/>
          <line x1="202.3" y1="387.8" x2="202.3" y2="567.8"/>
          <rect class="checkbox" x="102.7" y="455" width="49.8" height="50" rx="15"/>
        </g>
        <g class="row">
          <rect x="50.8" y="583.2" width="749.3" height="180" rx="21"/>
          <line x1="202.3" y1="583.2" x2="202.3" y2="763.2"/>
          <rect class="checkbox" x="102.7" y="651.5" width="49.8" height="50" rx="15"/>
        </g>
        <g class="row">
          <rect x="50.8" y="778.7" width="749.3" height="180.3" rx="21"/>
          <line x1="202.3" y1="778.7" x2="202.3" y2="959"/>
          <rect class="checkbox" x="102.7" y="847" width="49.8" height="50" rx="15"/>
        </g>
        <g class="row">
          <rect x="50.8" y="974.1" width="749.6" height="180.5" rx="21"/>
          <line x1="202.3" y1="974.1" x2="202.3" y2="1154.6"/>
          <rect class="checkbox" x="102.7" y="1042.5" width="49.8" height="50" rx="15"/>
        </g>
      </g>
    </svg>

    <h1 class="sheet-title"><span>To Do</span><span>List</span></h1>
  </main>
</body>
</html>
```